Falcrest security business card

Looking for a business card for my security company

Target Market(s)

Security

Industry/Entity Type

Security

Contact Information for Business Card

Name - Gil Marston. Title - General manager - direct 314 862.4490 website www. falcrestsecurityservices.example email - gil@ falcrestsecurityservices.example

Requirements
Must have
• Logo attached

```html
<!DOCTYPE html>
<html lang="en">
<head>
<meta charset="utf-8">
<title>Falcrest Security Services – Business Card</title>
<link rel="stylesheet" href="https://fonts.googleapis.com/css2?family=Montserrat:wght@600;700;800&family=Poppins:wght@400;500&display=swap">
<style>
  :root {
    --bg: #2b2b2d;
    --card-black: #060606;
    --card-white: #ffffff;
    --ink: #111111;
    --gold-dark: #a87826;
    --gold: #d6a94a;
    --gold-light: #f3d98c;
    --gold-gradient: linear-gradient(100deg, #a87826 0%, #e9c66e 35%, #b8862f 60%, #f3d98c 100%);
  }
  * { box-sizing: border-box; margin: 0; padding: 0; }
  html, body { width: 1200px; height: 900px; overflow: hidden; }
  body { background: var(--bg); position: relative; font-family: "Poppins", sans-serif; }

  .card {
    position: absolute;
    width: 620px;
    height: 354px;
    border-radius: 22px;
    overflow: hidden;
    box-shadow: 0 14px 30px rgba(0,0,0,.45);
  }

  /* Back side */
  .card--back { left: 60px; top: 60px; background: var(--card-black); }
  .card--back .brand {
    position: absolute; left: 0; right: 0; top: 118px;
    display: flex; align-items: center; justify-content: center; gap: 14px;
  }
  .brand__mark { width: 16px; height: 16px; border-radius: 50%; background: var(--gold); }
  .card--back .brand__name {
    font-family: "Montserrat", sans-serif; font-weight: 800;
    font-size: 52px; letter-spacing: 2px; color: var(--gold);
  }
  .card--back .tagline {
    position: absolute; left: 0; right: 0; top: 190px; text-align: center;
    font-family: "Montserrat", sans-serif; font-weight: 600;
    font-size: 12px; letter-spacing: 6px; color: var(--gold);
  }
  .card--back .web {
    position: absolute; left: 0; right: 0; bottom: 44px; text-align: center;
    font-size: 14px; color: var(--gold); letter-spacing: .3px;
  }

  /* Front side */
  .card--front { left: 520px; top: 486px; background: var(--card-white); }
  .front__panel {
    position: absolute; right: 0; top: 0; bottom: 0; width: 38%;
    background: var(--card-black);
  }
  .card--front .brand {
    position: absolute; left: 40px; top: 54px;
    display: flex; align-items: center; gap: 10px;
  }
  .card--front .brand__mark { background: var(--ink); width: 12px; height: 12px; }
  .card--front .brand__name {
    font-family: "Montserrat", sans-serif; font-weight: 800;
    font-size: 38px; letter-spacing: 1.5px; color: var(--ink);
  }
  .card--front .tagline {
    position: absolute; left: 64px; top: 104px;
    font-family: "Montserrat", sans-serif; font-weight: 600;
    font-size: 9px; letter-spacing: 5px; color: var(--ink);
  }
  .person {
    position: absolute; right: 30px; top: 40px; text-align: right;
    color: var(--gold);
  }
  .person__name {
    font-family: "Montserrat", sans-serif; font-weight: 700;
    font-size: 22px; letter-spacing: 1.5px;
  }
  .person__title {
    font-family: "Montserrat", sans-serif; font-weight: 700;
    font-size: 11px; letter-spacing: 2px; margin-top: 2px;
  }
  .person__rule {
    width: 60px; height: 2px; background: var(--gold-gradient);
    margin: 8px 0 0 auto;
  }
  .illustration {
    position: absolute; left: 300px; top: 138px; width: 290px; height: 100px;
    border-radius: 50px 40px 60px 30px;
    background: var(--gold-gradient);
  }
  .contact {
    position: absolute; left: 40px; bottom: 34px;
    list-style: none; color: var(--ink); font-size: 14.5px; line-height: 1.75;
  }
  .contact li { display: flex; align-items: center; gap: 10px; }
  .contact svg { width: 14px; height: 14px; flex: none; }
</style>
</head>
<body>

  <section class="card card--back" aria-label="Business card back">
    <div class="brand">
      <span class="brand__mark"></span>
      <span class="brand__name">FALCREST</span>
    </div>
    <p class="tagline">SECURITY SERVICES</p>
    <p class="web">www. falcrestsecurityservices.example</p>
  </section>

  <section class="card card--front" aria-label="Business card front">
    <div class="front__panel"></div>

    <div class="brand">
      <span class="brand__mark"></span>
      <span class="brand__name">FALCREST</span>
    </div>
    <p class="tagline">SECURITY SERVICES</p>

    <div class="person">
      <p class="person__name">GIL MARSTON</p>
      <p class="person__title">GENERAL MANAGER</p>
      <div class="person__rule"></div>
    </div>

    <div class="illustration" role="img" aria-label="Gold leaping big cat silhouette spanning the white and black halves"></div>

    <ul class="contact">
      <li>
        <svg viewBox="0 0 16 16" aria-hidden="true"><path fill="#d6a94a" d="M3.5 1.5l2.5 0 1 3.5-1.6 1.2a9 9 0 0 0 4.4 4.4L11 9l3.5 1v2.5c0 1-1 2-2 2C6.5 14.5 1.5 9.5 1.5 3.5c0-1 1-2 2-2z"/></svg>
        314 862.4490
      </li>
      <li>
        <svg viewBox="0 0 16 16" aria-hidden="true"><g fill="none" stroke="#d6a94a" stroke-width="1.4"><circle cx="8" cy="8" r="6.5"/><ellipse cx="8" cy="8" rx="2.8" ry="6.5"/><path d="M1.5 8h13M2.5 4.8h11M2.5 11.2h11"/></g></svg>
        www. falcrestsecurityservices.example
      </li>
      <li>
        <svg viewBox="0 0 16 16" aria-hidden="true"><rect x="1" y="3" width="14" height="10" fill="#d6a94a"/><path d="M1 3l7 5.5L15 3" fill="none" stroke="#fff" stroke-width="1.2"/></svg>
        gil@ falcrestsecurityservices.example
      </li>
    </ul>
  </section>

</body>
</html>
```